Copperleaf Motorized Shade Business Card

Hello, we've had our logo made. Now we are looking for a clean and cool looking business card. One side can just be the logo with any design elements that might look good with it. The other side will be Name, Phone Number and Email. There will not be an address on the card.

```html
<!DOCTYPE html>
<html lang="en">
<head>
<meta charset="utf-8">
<title>Copperleaf Motorized Shade – Business Card</title>
<link rel="stylesheet" href="https://fonts.googleapis.com/css2?family=Open+Sans:wght@400;600;700&display=swap">
<style>
  :root {
    --backdrop: #f3c232;
    --card-light: #ffffff;
    --card-dark: #3c3c3c;
    --brand-navy: #0f3d78;
    --brand-sun: #f7b500;
    --accent-blue: #1296dc;
    --text-light: #ffffff;
  }
  html, body {
    margin: 0;
    padding: 0;
    width: 1183px;
    height: 1200px;
    overflow: hidden;
    background: var(--backdrop);
    font-family: "Open Sans", Arial, sans-serif;
  }
  .canvas {
    position: relative;
    width: 1183px;
    height: 1200px;
  }
  .card {
    position: absolute;
    left: 161px;
    width: 860px;
    height: 557px;
    box-shadow: 0 10px 24px rgba(120, 80, 0, 0.25);
  }
  .card--front { top: 28px; background: var(--card-light); }
  .card--back  { top: 615px; background: var(--card-dark); }

  .brand {
    position: absolute;
    left: 0;
    right: 0;
    top: 200px;
    display: flex;
    justify-content: center;
    align-items: center;
    gap: 16px;
  }
  .brand__mark {
    width: 34px;
    height: 34px;
    background: var(--brand-sun);
  }
  .brand__name {
    margin: 0;
    color: var(--brand-navy);
    font-weight: 700;
    font-size: 58px;
    line-height: 1;
    letter-spacing: 0.5px;
  }
  .brand__tagline {
    position: absolute;
    left: 0;
    right: 0;
    top: 282px;
    text-align: center;
    margin: 0;
    color: var(--accent-blue);
    font-weight: 700;
    font-size: 16px;
    letter-spacing: 6px;
  }

  .person {
    position: absolute;
    left: 94px;
    top: 228px;
  }
  .person__name {
    margin: 0;
    color: var(--accent-blue);
    font-weight: 400;
    font-size: 50px;
    line-height: 1;
    letter-spacing: 1px;
  }
  .person__role {
    margin: 6px 0 0;
    color: var(--accent-blue);
    font-size: 29px;
    line-height: 1.1;
  }

  .contacts {
    position: absolute;
    left: 456px;
    top: 238px;
    margin: 0;
    padding: 0;
    list-style: none;
  }
  .contact {
    display: flex;
    align-items: center;
    gap: 16px;
    height: 36px;
    margin-bottom: 10px;
    color: var(--text-light);
    font-size: 20px;
    white-space: nowrap;
  }
  .contact__icon {
    width: 36px;
    height: 36px;
    flex: none;
  }
</style>
</head>
<body>
<main class="canvas">

  <section class="card card--front" aria-label="Card front">
    <div class="brand">
      <span class="brand__mark" aria-hidden="true"></span>
      <h1 class="brand__name">Copperleaf</h1>
    </div>
    <p class="brand__tagline">MOTORIZED SHADE</p>
  </section>

  <section class="card card--back" aria-label="Card back">
    <div class="person">
      <h2 class="person__name">DAREN HOLT</h2>
      <p class="person__role">sales manager</p>
    </div>

    <ul class="contacts">
      <li class="contact">
        <svg class="contact__icon" viewBox="0 0 36 36" aria-hidden="true">
          <circle cx="18" cy="18" r="18" fill="var(--accent-blue)"/>
          <rect x="10" y="12" width="16" height="12" fill="none" stroke="#fff" stroke-width="1.6"/>
          <polyline points="10,12 18,19 26,12" fill="none" stroke="#fff" stroke-width="1.6"/>
        </svg>
        <span>daren.holt@cplf-shades.example</span>
      </li>
      <li class="contact">
        <svg class="contact__icon" viewBox="0 0 36 36" aria-hidden="true">
          <circle cx="18" cy="18" r="18" fill="var(--accent-blue)"/>
          <g fill="none" stroke="#fff" stroke-width="1.4">
            <circle cx="18" cy="18" r="8"/>
            <ellipse cx="18" cy="18" rx="3.5" ry="8"/>
            <line x1="10" y1="18" x2="26" y2="18"/>
            <line x1="11.5" y1="14" x2="24.5" y2="14"/>
            <line x1="11.5" y1="22" x2="24.5" y2="22"/>
          </g>
        </svg>
        <span>www.cplf-shades.example</span>
      </li>
      <li class="contact">
        <svg class="contact__icon" viewBox="0 0 36 36" aria-hidden="true">
          <circle cx="18" cy="18" r="18" fill="var(--accent-blue)"/>
          <path d="M10 15 Q18 9 26 15 L24 18 L21 16 L15 16 L12 18 Z" fill="#fff"/>
          <rect x="12" y="18" width="12" height="8" rx="1.5" fill="#fff"/>
        </svg>
        <span>0044 55501234</span>
      </li>
    </ul>
  </section>

</main>
</body>
</html>
```